Tender / Request for Quotation response template

VELKOR42 is a small consulting company that works in management consulting with a particular emphasis on tourism, sport, major events and general commercial. our clients range from government , councils, private businesses and industry associations.

we are regularly asked to submit detailed quotes or tender responses and we use our own PowerPoint template to do so as we find it its generally easier to work with.

our website provides more detail : www.velkor42.com.au the colour of the blue in logo is #000033

our submissions range from 30 pages to 100 pages depending on the size and scale of the project - so we need flexibility with the templates.

Our submissions generally include cover page and table of contents and then
1. Project overview
2. About VELKOR42
3. The project team including bios
4. Initial Insights
5. importance of sustainability
6. Project methodology - example being
6.1 situation analysis
- research
- consultation and engagement
- relevant audits
- relevant economic analysis including graphs
- gap analysis
- SWOT
6.2 Issues and opportunities
6.3 draft report
6.4 final report
7. Case studies and previous relevant work
8. Project timeline
9. Project budget
10. Insurance and referees

we use many graphs and tables from excel and images generally sourced from the web. we also use icons as appropriate so we need graph templates - column, bar / pie etc and table templates.

the feel is on the formal corporate side given the size and scale of projects and clients but with bright and clear graphics and photos.

i have attached 2 copies of confidential submissions that we have made in recent weeks. one long form and one short form to give you an idea of the flexibility we need in the submission process.

if we are happy with the proposed PowerPoint tender submission template we would then look to have a similar one created to use in the development of the actual reports themselves .

hopefully this provides enough information but if not please reach out for more information

our logo and general format are in the attached examples

Target Market(s)

government, council, corporates and private businesses

Industry/Entity Type

management consulting with emphasis on tourism sport major events nd general commerical

Font styles to use
Other font styles liked:
• we usually use calbiri but open to other standard microsoft off the shelf fonts

Colors
0054AA
0677BA
7BADD7
CADEEF
E8F1F8
0094D4
00A9DD
6FCCEA
C7EBF8
E9F6FB

Requirements
Must have
• page for each of the sections detailed in the project brief. image placement - small and large, table and graph formats,

```html
<!DOCTYPE html>
<html lang="en">
<head>
<meta charset="UTF-8">
<title>Project Overview – VELKOR42</title>
<link rel="stylesheet" href="https://fonts.googleapis.com/css2?family=Montserrat:wght@400;500;600&display=swap">
<style>
  :root {
    --brand-blue: #0054AA;
    --ink: #1f1f1f;
    --page-top: #ffffff;
    --page-bottom: #b6cfe8;
    --footer-bg: #3d3d3d;
    --footer-text: #ffffff;
  }
  * { margin: 0; padding: 0; box-sizing: border-box; }
  html, body { width: 1200px; height: 900px; overflow: hidden; }
  body { font-family: "Montserrat", Arial, sans-serif; color: var(--ink); }

  .slide {
    position: relative;
    width: 1200px;
    height: 900px;
    background: linear-gradient(180deg, var(--page-top) 0%, #e6eff8 40%, var(--page-bottom) 100%);
    overflow: hidden;
  }

  .slide-header {
    position: absolute;
    top: 15px;
    left: 0;
    right: 0;
    height: 72px;
  }
  .title-accent {
    position: absolute;
    left: 0;
    top: 0;
    width: 12px;
    height: 72px;
    background: var(--brand-blue);
  }
  .slide-title {
    position: absolute;
    left: 26px;
    top: 11px;
    font-size: 39px;
    font-weight: 600;
    letter-spacing: 0.3px;
    color: var(--brand-blue);
    line-height: 1.2;
    white-space: nowrap;
  }

  .brand {
    position: absolute;
    right: 18px;
    top: 3px;
    display: flex;
    align-items: center;
    gap: 12px;
  }
  .brand-mark {
    width: 63px;
    height: 63px;
    border-radius: 50%;
    border: 3px solid var(--brand-blue);
  }
  .brand-name {
    font-size: 28px;
    font-weight: 500;
    color: var(--brand-blue);
    white-space: nowrap;
  }

  .slide-body {
    position: absolute;
    left: 50px;
    right: 26px;
    top: 137px;
  }
  .slide-body p {
    font-size: 19.6px;
    font-weight: 400;
    line-height: 33px;
    margin-bottom: 33px;
  }

  .slide-footer {
    position: absolute;
    left: 0;
    right: 0;
    bottom: 0;
    height: 50px;
    background: var(--footer-bg);
    color: var(--footer-text);
    display: flex;
    align-items: center;
    justify-content: space-between;
    padding: 0 16px;
    font-size: 20px;
    font-weight: 500;
  }
</style>
</head>
<body>
  <main class="slide">
    <header class="slide-header">
      <div class="title-accent"></div>
      <h1 class="slide-title">PROJECT OVERVIEW</h1>
      <div class="brand">
        <div class="brand-mark"></div>
        <span class="brand-name">VELKOR42</span>
      </div>
    </header>

    <section class="slide-body">
      <p>Lorem Ipsum is simply dummy text of the printing and typesetting industry. Lorem Ipsum has been the industry's standard dummy text ever since the 1500s, when an unknown printer took a galley of type and scrambled it to make a type specimen book. It has survived not only five centuries, but also the leap into electronic typesetting, remaining essentially unchanged. It was popularised in the 1960s with the release of Tranfex sheets containing Lorem Ipsum passages, and more recently with desktop publishing software like Quillon PageCraft including versions of Lorem Ipsum.</p>
      <p>Lorem Ipsum is simply dummy text of the printing and typesetting industry. Lorem Ipsum has been the industry's standard dummy text ever since the 1500s, when an unknown printer took a galley of type and scrambled it to make a type specimen book. It has survived not only five centuries, but also the leap into electronic typesetting, remaining essentially unchanged. It was popularised in the 1960s with the release of Tranfex sheets containing Lorem Ipsum passages, and more recently with desktop publishing software like Quillon PageCraft including versions of Lorem Ipsum.</p>
      <p>Lorem Ipsum is simply dummy text of the printing and typesetting industry. Lorem Ipsum has been the industry's standard dummy text ever since the 1500s, when an unknown printer took a galley of type and scrambled it to make a type specimen book. It has survived not only five centuries, but also the leap into electronic typesetting, remaining essentially unchanged. It was popularised in the 1960s with the release of Tranfex sheets containing Lorem Ipsum passages, and more recently with desktop publishing software like Quillon PageCraft including versions of Lorem Ipsum.</p>
    </section>

    <footer class="slide-footer">
      <span class="copyright">Copyright text here</span>
      <span class="page-number">Page : 01</span>
    </footer>
  </main>
</body>
</html>
```